Pine Ridge Dwellings Stationary and Simplified Embroidery Contest
Business Card, Letterhead, Envelope, Note Pad, Sticker, Embroidery
Pine Ridge Dwellings Stationary and Simplified Embroidery Contest -
Creative Brief
Professional
Wendell Marsh
Construction Manager
4812 Galloway Street Edmonton AB T5K 3R8
wendell@pineridgedwellings.example
www.pineridgedwellings.example
Please include some with light backgrounds as well as dark options... we want to be able to print a few cards so that not every card we hand out is the same! I would like to have 4-6 business card designs. The embroidery part would just be a simplified logo.
Comments/Blank space for notes to written on the business card. We have looked at a few designs for business cards and like the Logo and Name on the front with all the details on the back, but do be creative with this is by no means a rule!

```html
<!DOCTYPE html>
<html lang="en">
<head>
<meta charset="utf-8">
<title>Pine Ridge Dwellings Stationery</title>
<link href="https://fonts.googleapis.com/css2?family=Cinzel:wght@500;700&family=Lato:wght@400&display=swap" rel="stylesheet">
<style>
  :root{
    --backdrop:#efe9df;
    --paper:#ffffff;
    --cream:#fbf3da;
    --orange:#e59a22;
    --orange-deep:#c2740f;
    --green:#56633f;
    --green-deep:#3f4a2d;
    --ink:#4a3a26;
    --muted:#8a7a66;
    --rule:#d9c9a6;
  }
  *{box-sizing:border-box;margin:0;padding:0}
  html,body{width:1200px;height:446px;overflow:hidden;background:var(--backdrop)}
  .sheet{position:relative;width:1200px;height:446px;font-family:"Lato",sans-serif;color:var(--ink)}
  .piece{position:absolute;background:var(--paper);box-shadow:0 2px 6px rgba(60,40,20,.18);overflow:hidden}
  .piece svg.art{position:absolute;inset:0;width:100%;height:100%}
  .caption{position:absolute;font-family:"Cinzel",serif;font-size:7px;letter-spacing:.8px;color:var(--muted);text-transform:uppercase;white-space:nowrap}

  .brand{position:absolute;display:flex;flex-direction:column;align-items:center;gap:3px}
  .brand-dot{width:12px;height:12px;border-radius:50%;background:var(--orange-deep)}
  .brand-name{font-family:"Cinzel",serif;font-weight:700;font-size:6px;letter-spacing:.5px;color:var(--ink);white-space:nowrap}

  .contact{position:absolute;font-size:4.2px;line-height:6px;color:var(--muted);white-space:nowrap}
  .footer-line{position:absolute;left:0;right:0;text-align:center;font-size:4.2px;color:var(--muted);white-space:nowrap}

  /* business cards */
  .card-front{left:58px;top:175px;width:103px;height:89px;background:var(--cream)}
  .card-front .brand{left:24px;right:0;top:30px}
  .card-front .brand-dot{width:10px;height:10px}
  .card-front .brand-name{font-size:4.6px;letter-spacing:.3px}
  .card-back{left:58px;top:282px;width:103px;height:80px;background:var(--cream);border:1px solid var(--orange)}
  .note-lines{position:absolute;left:10px;right:10px;top:14px;display:flex;flex-direction:column;gap:12px}
  .note-lines span{display:block;height:1px;background:var(--rule)}

  /* letterheads */
  .letterhead-one{left:182px;top:12px;width:281px;height:408px}
  .letterhead-one .brand{left:88px;top:18px}
  .letterhead-one .contact{left:172px;top:18px}
  .letterhead-two{left:480px;top:12px;width:283px;height:408px}
  .letterhead-two .brand{left:84px;top:18px}
  .letterhead-two .footer-line{bottom:58px}

  /* envelopes */
  .envelope{left:828px;width:343px;height:90px}
  .envelope .brand{left:165px}
  .env-orange{top:7px;background:linear-gradient(180deg,var(--orange),var(--orange-deep))}
  .env-green{top:102px;background:var(--green)}
  .env-orange .brand-dot,.env-green .brand-dot{background:var(--green-deep)}
  .env-flap-white{top:200px;height:98px}
  .env-plain{top:312px;height:96px}
  .env-plain .brand{left:22px;top:10px}
</style>
</head>
<body>
<main class="sheet">

  <span class="caption" style="left:58px;top:163px">Business Card Front</span>
  <section class="piece card-front">
    <svg class="art" viewBox="0 0 103 89" preserveAspectRatio="none" aria-hidden="true">
      <path d="M0 0 H22 C12 30 12 60 22 89 H0 Z" fill="var(--orange)"/>
      <path d="M22 0 C12 30 12 60 22 89" fill="none" stroke="var(--green)" stroke-width="2"/>
    </svg>
    <div class="brand"><span class="brand-dot"></span><span class="brand-name">Pine Ridge Dwellings</span></div>
  </section>

  <section class="piece card-back">
    <div class="note-lines"><span></span><span></span><span></span><span></span><span></span></div>
  </section>
  <span class="caption" style="left:58px;top:372px">Business Card Back</span>

  <section class="piece letterhead-one">
    <svg class="art" viewBox="0 0 281 408" preserveAspectRatio="none" aria-hidden="true">
      <path d="M0 0 H34 C16 130 16 280 34 408 H0 Z" fill="var(--orange)"/>
      <path d="M34 0 C16 130 16 280 34 408" fill="none" stroke="var(--green)" stroke-width="4"/>
    </svg>
    <div class="brand"><span class="brand-dot"></span><span class="brand-name">Pine Ridge Dwellings</span></div>
    <div class="contact">
      4812 Galloway Street<br>Edmonton AB T5K 3R8<br>T 780 555 0142<br>wendell@pineridgedwellings.example<br>www.pineridgedwellings.example
    </div>
  </section>
  <span class="caption" style="left:290px;top:430px">Letterhead Option 1</span>

  <section class="piece letterhead-two">
    <svg class="art" viewBox="0 0 283 408" preserveAspectRatio="none" aria-hidden="true">
      <path d="M0 408 V400 C110 398 210 388 283 362 V408 Z" fill="var(--orange)"/>
      <path d="M0 396 C110 394 210 383 283 356" fill="none" stroke="var(--green)" stroke-width="3"/>
    </svg>
    <div class="brand"><span class="brand-dot"></span><span class="brand-name">Pine Ridge Dwellings</span></div>
    <p class="footer-line">4812 Galloway Street Edmonton AB T5K 3R8 · T 780 555 0142 · www.pineridgedwellings.example</p>
  </section>
  <span class="caption" style="left:588px;top:430px">Letterhead Option 2</span>

  <section class="piece envelope env-orange">
    <svg class="art" viewBox="0 0 343 90" preserveAspectRatio="none" aria-hidden="true">
      <path d="M0 0 L171 44 L343 0" fill="none" stroke="rgba(0,0,0,.15)" stroke-width="1"/>
    </svg>
    <div class="brand" style="top:12px"><span class="brand-dot"></span></div>
  </section>
  <section class="piece envelope env-green">
    <svg class="art" viewBox="0 0 343 90" preserveAspectRatio="none" aria-hidden="true">
      <path d="M0 0 L171 44 L343 0" fill="none" stroke="rgba(0,0,0,.2)" stroke-width="1"/>
    </svg>
    <div class="brand" style="top:12px"><span class="brand-dot"></span></div>
  </section>
  <section class="piece envelope env-flap-white">
    <svg class="art" viewBox="0 0 343 98" preserveAspectRatio="none" aria-hidden="true">
      <path d="M0 0 L171 48 L343 0" fill="none" stroke="var(--rule)" stroke-width="1"/>
      <path d="M0 98 L130 52 M343 98 L212 52" fill="none" stroke="var(--rule)" stroke-width="1"/>
    </svg>
    <div class="brand" style="top:12px"><span class="brand-dot"></span></div>
  </section>
  <section class="piece envelope env-plain">
    <svg class="art" viewBox="0 0 343 96" preserveAspectRatio="none" aria-hidden="true">
      <path d="M0 96 V90 C120 90 240 84 343 70 V96 Z" fill="var(--orange)"/>
      <path d="M0 86 C120 86 240 80 343 65" fill="none" stroke="var(--green)" stroke-width="2"/>
    </svg>
    <div class="brand"><span class="brand-dot"></span><span class="brand-name">Pine Ridge Dwellings</span></div>
  </section>
  <span class="caption" style="left:960px;top:430px">Envelope Options</span>

</main>
</body>
</html>
```